"VaduMakers" Graphic Design Project

We are a new business creating bath/ body/beauty products. We need label designs for men "Lusto for Men " and women- "Lusto for Women" . Since the collection called Lusto will be used for both- we'd like the labels to look similar but separating the gender look- maybe by a same color variation. Our bottles are amber in color , so we like the beiges, cream, and earthy warm tones - greens- brown-orange- yellow-colors. The labels are for 8 oz amber cosmo round bottles. The height is 7.32inches and the diameter is 1.85 inches.
Our starting line will be Lusto for Men ( Silk Body Wash, Silk Body Lotion and Body Mist) and the same for Lusto for Women.
Updates

Target Market(s)

Our target audience is between 30 to 60 years of age. Salons and private consumers.
I am including attached sample of what was started by me.

Industry/Entity Type

Business

Requirements
Must have
• We would like to incorporate the company name- VaduMakers along with the name of the product- which will be Lusto for Men or Lusto for Women on each label.

On label with company name or somewhere on label we would like a tree to symbolize the beginning, but we are open to suggestions.

```html
<!DOCTYPE html>
<html lang="en">
<head>
<meta charset="utf-8">
<title>VaduMakers – Lusto Labels</title>
<link href="https://fonts.googleapis.com/css2?family=Cinzel:wght@400;600&display=swap" rel="stylesheet">
<style>
  :root {
    --page: #ffffff;
    --bark: #3b2512;
    --bark-deep: #2a190b;
    --bark-soft: #4e3319;
    --gold: #e9b52a;
    --gold-pale: #f2d27a;
    --band: #f5c431;
    --band-deep: #e0a818;
    --band-light: #fcd23f;
    --ink: #3a2410;
    --symbol: #8a6a3c;
  }
  * { box-sizing: border-box; margin: 0; padding: 0; }
  html, body { width: 1200px; height: 1000px; overflow: hidden; background: var(--page); }
  .canvas {
    position: relative; width: 1200px; height: 1000px;
    font-family: "Cinzel", "Times New Roman", serif;
    font-variant: small-caps;
  }
  .label {
    position: absolute; overflow: hidden;
    background: linear-gradient(180deg, var(--bark-soft) 0%, var(--bark) 45%, var(--bark-deep) 100%);
    color: var(--gold);
    text-align: center;
    box-shadow: 0 2px 6px rgba(0,0,0,.25);
  }
  .label--men   { left: 115px; top: 300px; width: 205px; height: 615px; }
  .label--back  { left: 483px; top: 305px; width: 234px; height: 630px; }
  .label--women { left: 868px; top: 310px; width: 205px; height: 605px; }

  .label__frame {
    position: absolute; inset: 6px 6px 6px 6px;
    border: 1px solid var(--gold); pointer-events: none; z-index: 3;
  }
  .brand-mark {
    position: absolute; left: 50%; top: 30px; transform: translateX(-50%);
    width: 14px; height: 14px; border-radius: 50%; background: var(--gold);
  }
  .brand-name {
    position: absolute; left: 0; right: 0; top: 108px;
    font-size: 15px; letter-spacing: .5px; color: var(--gold-pale);
  }
  .product-name {
    position: absolute; left: 0; right: 0; top: 188px;
    font-size: 38px; font-weight: 600; letter-spacing: 1px; color: var(--gold-pale);
  }
  .product-audience {
    position: absolute; left: 0; right: 0; top: 236px;
    font-size: 14px; line-height: 17px; color: var(--gold-pale);
  }
  .symbol-area {
    position: absolute; left: 12px; top: 285px; width: 170px; height: 150px;
    background: radial-gradient(circle at 45% 55%, var(--bark-deep) 0 30%, var(--symbol) 31% 48%, rgba(138,106,60,0) 60%);
    opacity: .9;
  }
  .band-art { position: absolute; left: 0; bottom: 0; width: 100%; }
  .band-title {
    position: absolute; left: 0; right: 0; top: 440px;
    font-size: 16px; color: var(--ink); z-index: 2;
  }
  .label--women .band-title { top: 432px; }
  .volume {
    position: absolute; left: 0; right: 0; bottom: 17px;
    font-size: 7px; color: var(--ink); z-index: 2;
  }

  /* back label */
  .back-content { position: absolute; left: 14px; right: 14px; top: 48px; }
  .back-brand { font-size: 11px; color: var(--gold-pale); }
  .back-intro { margin-top: 6px; font-size: 9.5px; line-height: 12px; color: var(--gold-pale); }
  .back-dot { display: block; width: 8px; height: 8px; margin: 9px auto 4px; border-radius: 50%; background: var(--gold); }
  .back-heading { font-size: 12.5px; color: var(--gold-pale); margin-top: 2px; }
  .back-text { font-size: 9px; line-height: 11.5px; color: var(--gold-pale); margin-top: 3px; }
  .back-heading--spaced { margin-top: 14px; }
  .ingredients { font-size: 6.3px; line-height: 8.5px; color: var(--gold-pale); margin-top: 3px; }
  .back-small { font-size: 7.5px; color: var(--gold-pale); margin-top: 12px; }
  .back-address { font-size: 6.8px; line-height: 8.5px; color: var(--gold-pale); margin-top: 12px; }
  .back-strip {
    position: absolute; left: 0; right: 0; bottom: 0; height: 44px;
    background: linear-gradient(180deg, var(--band-deep), var(--band));
  }
  .back-web {
    position: absolute; left: 0; right: 0; bottom: 18px;
    font-size: 7px; color: var(--ink); z-index: 4;
  }
</style>
</head>
<body>
<div class="canvas">

  <section class="label label--men" aria-label="Lusto for Men front label">
    <span class="brand-mark" aria-hidden="true"></span>
    <div class="brand-name">VaduMakers</div>
    <div class="product-name">Lusto</div>
    <div class="product-audience">for<br>Men</div>
    <div class="symbol-area" role="img" aria-label="Large soft male gender symbol decoration"></div>
    <svg class="band-art" viewBox="0 0 205 210" height="210" aria-hidden="true">
      <path d="M0 28 Q102 0 205 28 L205 210 L0 210 Z" fill="var(--band-light)"/>
      <path d="M0 28 Q102 0 205 28 L205 92 Q102 112 0 92 Z" fill="var(--band)"/>
      <path d="M0 92 Q102 112 205 92" fill="none" stroke="var(--band-deep)" stroke-width="2"/>
      <path d="M14 192 Q102 150 191 192" fill="none" stroke="var(--band-deep)" stroke-width="1"/>
    </svg>
    <div class="band-title">Silk Body Wash</div>
    <div class="volume">8.25 fl. oz. / 244mL</div>
    <div class="label__frame"></div>
  </section>

  <section class="label label--back" aria-label="Back label">
    <div class="back-content">
      <span class="back-dot" aria-hidden="true"></span>
      <div class="back-brand">VaduMakers</div>
      <p class="back-intro">Our Nourishing Silk Body Wash will engulf you in luxurious lather as it gently cleanses your delicate skin leaving it soft as silk.</p>
      <span class="back-dot" aria-hidden="true"></span>
      <div class="back-heading">Directions</div>
      <p class="back-text">Apply to skin while damp with sponge or wash cloth.<br>Rinse well.</p>
      <span class="back-dot" aria-hidden="true"></span>
      <div class="back-heading">Warnings/Cautions</div>
      <p class="back-text">For external use only.<br>Avoid contact with eyes.</p>
      <div class="back-heading back-heading--spaced">Ingredients:</div>
      <p class="ingredients">Purified water, sodium olefin sulfonate, cocamidopropyl betaine, coconut based cleanser, organic aloe leaf juice, vegetable glycerin, sea salt, polysorbate 20, sunflower seed oil, vitamin E, oat protein, potassium sorbate, phenoxyethanol, organic chamomile extract, organic calendula flower extract, xanthan gum, vitamin C, baking soda, citric acid, natural fragrance.</p>
      <div class="back-small">Not tested on animals</div>
      <div class="back-small">Made in USA</div>
      <p class="back-address">VaduMakers<br>Bath ~ Body - Home<br>Harbor Bay, FL 30001<br>Shop 24/7</p>
    </div>
    <div class="back-strip"></div>
    <div class="back-web">www.vadumakers.com</div>
    <div class="label__frame"></div>
  </section>

  <section class="label label--women" aria-label="Lusto for Women front label">
    <span class="brand-mark" aria-hidden="true"></span>
    <div class="brand-name">VaduMakers</div>
    <div class="product-name">Lusto</div>
    <div class="product-audience">for<br>Women</div>
    <div class="symbol-area" role="img" aria-label="Large soft female gender symbol decoration"></div>
    <svg class="band-art" viewBox="0 0 205 210" height="210" aria-hidden="true">
      <path d="M0 28 Q102 0 205 28 L205 210 L0 210 Z" fill="var(--band-light)"/>
      <path d="M0 28 Q102 0 205 28 L205 92 Q102 112 0 92 Z" fill="var(--band)"/>
      <path d="M0 92 Q102 112 205 92" fill="none" stroke="var(--band-deep)" stroke-width="2"/>
      <path d="M14 192 Q102 150 191 192" fill="none" stroke="var(--band-deep)" stroke-width="1"/>
    </svg>
    <div class="band-title">Silk Body Wash</div>
    <div class="volume">8.25 fl. oz. / 244mL</div>
    <div class="label__frame"></div>
  </section>

</div>
</body>
</html>
```